Custom Wordpress Theme - Original and Professional

We are a Kestrel IT Consulting firm that provide small and medium business in Australia three different levels of IT service.
We are looking for a developer who will create a customised, original and professional wordpress theme. We are looking for the developer to create a professional, clean, clear and simple theme with a stylish layout, images and icons.
Our three services are: IT support | IT Services | IT Solutions and we would like to clearly differentiate the difference in each level of service in as few words as possible.
IT Support is the ad hock “call us, when you need us” service, that smaller business or those with minimal issues use.
IT service is the unlimited service, that business with existing (and well maintained) IT systems choose and is both flexible and scalable including no contracts or paperwork required.
IT solutions are the unlimited service that businesses that need new or updated infrastructure choose and it includes all the hardware, software and services with no contracts or any ongoing commitment.
The main page on the web site will attract the visitor to choose the right “service level” for their business and then we will have a dedicated page for each service and another page for a comparison (table) to compare all three services.
Lastly we will need a contact us page that has both office locations (Sydney and Melbourne), contact phone numbers and an email form.
Items we are focused on for this project are: 1. Images, 2.Icons 3. Layout.
In summary we are looking for a custom WordPress theme into a 6 page (Home, IT Support, IT Services, IT Solutions, Compare Service levels and Contact us) website. The design must include relevant images and icons and be clear, simple, professional and sleek.

Thank you for your time and creativity and I look forward to working with you!

Target Market(s)

Small and Medium businesses in Australia

Industry/Entity Type

Boutique

Requirements
Must have
• - 6 Pages layout: Home, IT support, IT services, IT Solutions, Compare service levels and Contact us
- Images, Layout and Icons.
- Clean, Clear, Simple, Elegant, Stylish.
Nice to have
• - Some text (if possible but not required).
Should not have
• - Complexity.
- Confusing layout.
- Generic non matching images and icons.

```html
<!DOCTYPE html>
<html lang="en">
<head>
<meta charset="utf-8">
<title>Kestrel IT Consulting</title>
<link rel="stylesheet" href="https://fonts.googleapis.com/css2?family=Bebas+Neue&family=Roboto+Condensed:wght@300;400&display=swap">
<style>
:root{
  --ink:#2e2e2e;
  --navy:#1d4f6e;
  --deep:#154666;
  --sky:#3a8fc4;
  --nav:#7f9db2;
  --hero-a:#f4f7f9;
  --hero-b:#c9d8e3;
  --hero-c:#7d9db4;
  --paper:#ffffff;
  --muted:#7a7a7a;
  --heading:"Bebas Neue", sans-serif;
  --body:"Roboto Condensed", sans-serif;
}
*{box-sizing:border-box;margin:0;padding:0}
html,body{width:1090px;height:1200px;overflow:hidden;background:var(--paper)}
.page{position:relative;width:1090px;height:1200px;overflow:hidden;background:var(--paper);font-family:var(--body);color:var(--ink)}

.site-header{position:absolute;left:0;top:0;width:1090px;height:110px;background:#f6f8fa}
.brand{position:absolute;display:flex;align-items:center;gap:10px}
.brand-mark{display:block;background:var(--sky)}
.brand-name{font-family:var(--heading);color:var(--navy);line-height:.9}
.site-header .brand{left:147px;top:22px}
.site-header .brand-mark{width:62px;height:62px}
.site-header .brand-name{font-size:44px;width:190px}
.help{position:absolute;right:155px;top:24px;text-align:right;font-family:var(--heading);color:var(--navy)}
.help-label{font-size:18px;color:var(--sky);letter-spacing:.5px}
.help-line{display:flex;align-items:center;gap:8px;font-size:30px;line-height:1}

.main-nav{position:absolute;left:0;top:110px;width:1090px;height:40px;background:var(--nav);display:flex;align-items:center;padding-left:175px;z-index:2}
.main-nav a{font-family:var(--heading);font-size:19px;color:#fff;text-decoration:none;letter-spacing:.3px}
.main-nav .sep{width:2px;height:18px;background:#fff;margin:0 22px}

.hero{position:absolute;left:0;top:110px;width:1090px;height:425px}
.hero-art{position:absolute;inset:0;background:
  radial-gradient(circle at 31% 38%, var(--hero-c) 0, #a9bfcf 17%, transparent 30%),
  linear-gradient(100deg, var(--hero-b) 0%, var(--hero-a) 45%, #e6edf2 100%)}
.hero-copy{position:absolute;right:152px;top:148px;text-align:right;font-family:var(--body);color:var(--deep)}
.hero-kicker{font-weight:300;font-size:33px;line-height:1}
.hero-title{font-family:var(--heading);font-size:74px;line-height:.95;color:var(--deep)}
.hero-sub{font-weight:300;font-size:31px;line-height:1;color:var(--sky)}
.cta{position:absolute;left:582px;top:303px;width:353px;height:91px;border-radius:3px;border:2px solid #5fa6d3;
  background:linear-gradient(180deg,#2b6c97 0%,#0f3f60 100%);color:#fff;text-align:center;font-family:var(--heading)}
.cta-label{font-size:23px;margin-top:7px;letter-spacing:.3px}
.cta-number{font-size:60px;line-height:.9}

.services{position:absolute;left:0;top:535px;width:1090px;height:205px}
.service{position:absolute;top:13px;height:192px;text-align:center;background:var(--paper)}
.service+.service{box-shadow:-10px 0 14px -10px rgba(0,0,0,.25)}
.service-1{left:148px;width:262px}
.service-2{left:416px;width:254px}
.service-3{left:676px;width:266px}
.service svg{display:block;margin:6px auto 0;height:110px}
.service-title{font-family:var(--heading);font-size:31px;color:var(--navy);margin-top:16px}
.rule{position:absolute;left:90px;width:910px;height:14px;background:radial-gradient(ellipse at center top,rgba(0,0,0,.12),transparent 70%)}
.rule-1{top:740px}.rule-2{top:1008px}

.welcome{position:absolute;left:200px;top:790px;width:690px;text-align:center}
.welcome h1{font-family:var(--heading);font-weight:400;font-size:55px;color:var(--ink);line-height:1;letter-spacing:.3px}
.welcome p{font-weight:300;font-size:17.5px;line-height:21px;color:#333;margin-top:12px}

.site-footer .brand{left:440px;top:1063px}
.site-footer .brand-mark{width:52px;height:52px}
.site-footer .brand-name{font-size:35px;width:150px}
.footer-nav{position:absolute;left:0;top:1144px;width:1090px;display:flex;justify-content:center;align-items:center;font-size:11px;color:var(--muted);text-transform:uppercase;letter-spacing:.3px}
.footer-nav a{color:var(--muted);text-decoration:none}
.footer-nav .sep{margin:0 20px}
</style>
</head>
<body>
<div class="page">
  <header class="site-header">
    <div class="brand"><span class="brand-mark"></span><span class="brand-name">Kestrel IT Consulting</span></div>
    <div class="help">
      <div class="help-label">Need help call us</div>
      <div class="help-line">
        <svg width="36" height="36" viewBox="0 0 36 36" fill="none" stroke="var(--navy)" stroke-width="3"><path d="M6 20V16a12 12 0 0 1 24 0v4"/><rect x="3" y="18" width="6" height="10" rx="2" fill="var(--navy)"/><rect x="27" y="18" width="6" height="10" rx="2" fill="var(--navy)"/><path d="M30 28c0 4-5 5-10 5" stroke-width="2"/></svg>
        <span>1-800-555-0142</span>
      </div>
    </div>
  </header>

  <nav class="main-nav">
    <a href="#">Home</a><span class="sep"></span>
    <a href="#">IT Support</a><span class="sep"></span>
    <a href="#">IT Services</a><span class="sep"></span>
    <a href="#">IT Solutions</a><span class="sep"></span>
    <a href="#">Compare Service Levels</a><span class="sep"></span>
    <a href="#">Contact Us</a>
  </nav>

  <section class="hero">
    <div class="hero-art" role="img" aria-label="Globe resting on open laptops with business people in conversation, blue toned"></div>
    <div class="hero-copy">
      <div class="hero-kicker">UT WISI ENIM</div>
      <div class="hero-title">UT DOLOR ADMINIM</div>
      <div class="hero-sub">LOBORTIS NISL UT ALIQUIP</div>
    </div>
    <div class="cta">
      <div class="cta-label">Call us now for a consultation</div>
      <div class="cta-number">1-800-555-0142</div>
    </div>
  </section>

  <section class="services">
    <div class="service service-1">
      <svg viewBox="0 0 120 110" width="120">
        <g fill="var(--navy)">
          <circle cx="46" cy="66" r="24" fill="none" stroke="var(--navy)" stroke-width="12" stroke-dasharray="9 6.1"/>
          <circle cx="46" cy="66" r="20"/>
          <circle cx="84" cy="32" r="17" fill="none" stroke="var(--navy)" stroke-width="10" stroke-dasharray="7 5.3"/>
          <circle cx="84" cy="32" r="14"/>
        </g>
        <circle cx="46" cy="66" r="8" fill="#fff"/>
        <circle cx="84" cy="32" r="6" fill="#fff"/>
      </svg>
      <div class="service-title">IT Services</div>
    </div>
    <div class="service service-2">
      <svg viewBox="0 0 120 110" width="120" fill="none" stroke="var(--navy)" stroke-width="9">
        <path d="M22 60V50a38 38 0 0 1 76 0v10"/>
        <rect x="12" y="50" width="20" height="32" rx="7" fill="var(--navy)" stroke="none"/>
        <rect x="88" y="50" width="20" height="32" rx="7" fill="var(--navy)" stroke="none"/>
        <path d="M98 80c0 14-16 20-30 20" stroke-width="6"/>
        <circle cx="64" cy="100" r="7" fill="var(--navy)" stroke="none"/>
      </svg>
      <div class="service-title">IT Support</div>
    </div>
    <div class="service service-3">
      <svg viewBox="0 0 120 110" width="120" stroke="var(--navy)" stroke-linecap="round">
        <g stroke-width="7">
          <line x1="60" y1="4" x2="60" y2="16"/>
          <line x1="22" y1="20" x2="30" y2="28"/><line x1="98" y1="20" x2="90" y2="28"/>
          <line x1="6" y1="52" x2="18" y2="52"/><line x1="102" y1="52" x2="114" y2="52"/>
          <line x1="22" y1="84" x2="30" y2="76"/><line x1="98" y1="84" x2="90" y2="76"/>
        </g>
        <path d="M60 28a24 24 0 0 0-14 43v9h28v-9a24 24 0 0 0-14-43z" fill="var(--navy)" stroke="none"/>
        <rect x="48" y="84" width="24" height="6" rx="2" fill="var(--navy)" stroke="none"/>
        <rect x="52" y="93" width="16" height="6" rx="3" fill="var(--navy)" stroke="none"/>
      </svg>
      <div class="service-title">IT Solutions</div>
    </div>
  </section>
  <div class="rule rule-1"></div>

  <section class="welcome">
    <h1>Welcome to Kestrel IT Consulting</h1>
    <p>Ut wisi enim ad minim veniam, quis nostrud exerci tation ullamcorper suscipit lobortis nisl ut aliquip ex ea commodo consequat. Duis autem vel eum iriure dolor in hendrerit in vulputate velit esse molestie consequat, vel illum dolore eu feugiat nulla facilisis at vero eros et accumsan et iusto odio dignissim qui blandit praesent luptatum zzril delenit augue duis dolore te feugait nulla Ut wisi enim ad minim veniam, quis nostrud exerci tation ullamcorper suscipit lobortis nisl ut aliquip ex ea commodo consequat.</p>
  </section>
  <div class="rule rule-2"></div>

  <footer class="site-footer">
    <div class="brand"><span class="brand-mark"></span><span class="brand-name">Kestrel IT Consulting</span></div>
    <nav class="footer-nav">
      <a href="#">About</a><span class="sep">|</span>
      <a href="#">Advertise</a><span class="sep">|</span>
      <a href="#">Add your site</a><span class="sep">|</span>
      <a href="#">Privacy policy</a><span class="sep">|</span>
      <a href="#">Contact us</a>
    </nav>
  </footer>
</div>
</body>
</html>
```